MoveNest Landing Page

We need to freshen up our homepage.

The company is MoveNest.com. We provide cloud-based management software for class venues - dance, yoga, martial arts, etc.

The challenge here is to create something that's simultaneously lighthearted and professional. We want our customers to know that the software is easy, fun and non-intimidating, but also powerful enough to handle whatever they throw at it.

Page content can remain the same as it is now. Feel free to move things around, manipulate it however you like.

We like our logo, but feel free to manipulate it as part of your design. Fonts used in the logo are Futura Extra Bold and Rockwell.

NOTE: The default screenshot in the homepage video is NOT our branding choice, it just happens to be the default freeze frame from vidloop.. Feel free to ignore it altogether in your design. We are not affiliated with that character, or the app that we used to create the vid.
Updates

Project Deadline Extended
Reason: We are extending this contest by request. Out of 65 designs, so far we only really like 4. There's still a good chance to win this contract! Please submit your very best :) Owen

Target Market(s)

Studio owners who are not necessarily tech savvy.

Industry/Entity Type

Software

Requirements
Must have
• Look and feel of a modern web app.

Delivery in a layered PSD.

```html
<!DOCTYPE html>
<html lang="en">
<head>
<meta charset="utf-8">
<title>MoveNest – Manage Your Classes Online</title>
<link rel="stylesheet" href="https://fonts.googleapis.com/css2?family=Open+Sans:wght@400;600;700;800&display=swap">
<style>
:root{
  --ink:#3b4a52;
  --muted:#7c8a90;
  --teal:#2c8e9c;
  --teal-dark:#1f6f7c;
  --mint:#e3f4f0;
  --blue:#3b8fcb;
  --green:#8cc63f;
  --green-dark:#74aa2c;
  --band:#e6e9ea;
  --price-bg:#5aaab4;
  --footer:#3a6a9c;
  --orange:#f39a2b;
  --white:#fff;
}
*{box-sizing:border-box;margin:0;padding:0}
html,body{width:889px;height:1200px;overflow:hidden}
body{font-family:"Open Sans",Arial,sans-serif;color:var(--ink);background:var(--white);position:relative}
.wrap{width:889px;height:1200px;position:relative}

/* header */
.site-header{height:56px;display:flex;align-items:center;justify-content:space-between;padding:0 60px 0 40px}
.brand{display:flex;align-items:center;gap:7px;font-weight:800;font-size:26px;color:var(--teal);letter-spacing:-.5px}
.brand-dot{width:12px;height:12px;border-radius:50%;background:var(--green)}
.main-nav{display:flex;align-items:center;gap:20px;font-size:11px;font-weight:600;color:var(--ink)}
.btn-start{background:var(--blue);color:var(--white);padding:6px 11px;border-radius:2px;font-size:10px}

/* hero */
.hero{height:290px;background:var(--mint);position:relative;padding:18px 0 0 90px;display:flex;gap:38px}
.video{width:440px;height:245px;border:4px solid var(--white);box-shadow:0 2px 6px rgba(0,0,0,.15);
  background:linear-gradient(160deg,#bfe6c9 0%,#a9d8e6 60%,#d7ece0 100%);position:relative}
.video-bar{position:absolute;top:0;left:0;right:0;height:22px;background:rgba(0,0,0,.55);color:var(--white);font-size:10px;padding:4px 8px}
.video-play{position:absolute;left:50%;top:50%;transform:translate(-50%,-50%)}
.hero-copy{width:260px;padding-top:14px}
.hero-title{font-size:18px;line-height:1.35;font-weight:700;color:var(--teal);text-transform:uppercase}
.btn-setup{display:inline-block;margin-top:26px;background:var(--green);color:var(--white);font-weight:700;font-size:14px;padding:12px 34px;border-radius:3px;box-shadow:0 3px 0 var(--green-dark)}
.dots{position:absolute;left:290px;bottom:10px;display:flex;gap:6px}
.dots span{width:7px;height:7px;border-radius:50%;background:#b9cfcb}
.dots span.on{background:var(--teal)}

/* features */
.features{padding:20px 60px 0;text-align:center}
.section-title{font-size:14px;font-weight:700;letter-spacing:1px;color:var(--teal)}
.feature-grid{display:grid;grid-template-columns:repeat(4,1fr);gap:26px;margin-top:18px}
.feature-icon{width:44px;height:36px;margin:0 auto;border-radius:50%;background:linear-gradient(#c8d3d6,#9fb1b6)}
.feature h3{font-size:12px;font-weight:700;color:var(--teal);margin-top:8px}
.feature p{font-size:9px;line-height:1.4;color:var(--muted);margin-top:4px}

/* about band */
.about{position:absolute;top:552px;left:0;width:889px;height:138px;background:var(--band);display:flex;gap:30px;padding:8px 60px 0 90px}
.about-card{width:420px;height:122px;background:var(--white);padding:8px 24px;text-align:center;box-shadow:0 1px 4px rgba(0,0,0,.12)}
.about-card h2{font-size:13px;font-weight:600;color:var(--ink)}
.about-card .brand{justify-content:center;margin:3px 0 4px;font-size:24px}
.about-card p{font-size:8.5px;line-height:1.45;color:var(--muted);text-align:left}
.perks{list-style:none;padding-top:6px}
.perks li{font-size:10.5px;font-weight:700;color:var(--teal);display:flex;align-items:center;gap:7px;height:20px}
.perks li small{font-size:8px;font-weight:400;color:var(--muted)}

/* pricing */
.pricing{position:absolute;top:690px;left:0;width:889px;height:420px;background:var(--price-bg);padding:42px 60px 0}
.plans{display:grid;grid-template-columns:1fr 1fr 1fr;gap:18px}
.plan{background:rgba(255,255,255,.92);padding:18px 22px;height:350px}
.plan.featured{background:var(--white);margin-top:-10px;height:370px;box-shadow:0 3px 10px rgba(0,0,0,.2);border-top:4px solid var(--teal)}
.plan h3{text-align:center;font-size:17px;font-weight:600;color:var(--teal);letter-spacing:.5px}
.price{text-align:center;font-size:26px;font-weight:800;color:var(--green);margin:4px 0 14px}
.price small{font-size:10px;font-weight:400;color:var(--muted)}
.plan ul{list-style:none}
.plan li{font-size:9.5px;height:21px;display:flex;align-items:center;gap:7px;color:var(--ink);border-bottom:1px solid #eef1f2}
.trial{position:absolute;right:20px;bottom:18px;width:70px;height:62px;background:var(--orange);color:var(--white);text-align:center;border-radius:3px;padding-top:7px;font-weight:800;line-height:1}
.trial span{display:block;font-size:10px}
.trial b{display:block;font-size:20px}

/* footer */
.site-footer{position:absolute;top:1110px;left:0;width:889px;height:90px;background:var(--footer);color:#dce7f2;padding:22px 60px}
.footer-row{display:flex;justify-content:space-between;font-size:10px}
.footer-links{display:flex;gap:8px}
.copyright{font-size:9px;margin-top:12px;color:#b7c9dc}
</style>
</head>
<body>
<div class="wrap">

<header class="site-header">
  <div class="brand"><span>MoveNest</span><span class="brand-dot"></span></div>
  <nav class="main-nav">
    <span>HOME</span><span>LOGIN</span><span>HELP</span><span class="btn-start">GET STARTED</span>
  </nav>
</header>

<section class="hero">
  <div class="video" role="img" aria-label="Introductory product video still, hosted on vidloop">
    <div class="video-bar">Introducing MoveNest</div>
    <svg class="video-play" width="56" height="40" viewBox="0 0 56 40"><rect width="56" height="40" rx="9" fill="#222" fill-opacity=".75"/><path d="M22 12 L36 20 L22 28 Z" fill="#fff"/></svg>
  </div>
  <div class="hero-copy">
    <h1 class="hero-title">The easiest way to manage your classes and accept payments online.</h1>
    <span class="btn-setup">5 MINUTE SETUP!</span>
  </div>
  <div class="dots"><span class="on"></span><span></span><span></span></div>
</section>

<section class="features">
  <h2 class="section-title">CLOUD BASED MANAGEMENT SOFTWARE</h2>
  <div class="feature-grid">
    <div class="feature"><div class="feature-icon" role="img" aria-label="Class venue icon"></div><h3>CLASS VENUES</h3><p>Simple tools to run every class from one clean dashboard.</p></div>
    <div class="feature"><div class="feature-icon" role="img" aria-label="Dance studio icon"></div><h3>CLASS VENUES</h3><p>Schedules, rosters and payments kept neatly in one place.</p></div>
    <div class="feature"><div class="feature-icon" role="img" aria-label="Yoga pose icon"></div><h3>YOGA</h3><p>Let students book their next session in just one click.</p></div>
    <div class="feature"><div class="feature-icon" role="img" aria-label="Martial arts icon"></div><h3>MARTIAL ARTS</h3><p>Track belts, attendance and memberships without any paperwork.</p></div>
  </div>
</section>

<section class="about">
  <div class="about-card">
    <h2>What is MoveNest?</h2>
    <div class="brand"><span>MoveNest</span><span class="brand-dot"></span></div>
    <p>MoveNest is the easiest and most affordable way to manage your class studio or venue. We help simplify your daily tasks by leveraging the power of the internet, saving you time and money. Anyone can learn to use MoveNest with our clean, common sense website.</p>
  </div>
  <ul class="perks">
    <li><svg width="10" height="10"><path d="M1 5 L4 8 L9 2" stroke="#8cc63f" stroke-width="2" fill="none"/></svg>WEB BASED, <small>access anywhere</small></li>
    <li><svg width="10" height="10"><path d="M1 5 L4 8 L9 2" stroke="#8cc63f" stroke-width="2" fill="none"/></svg>INTUITIVE, <small>easy to use</small></li>
    <li><svg width="10" height="10"><path d="M1 5 L4 8 L9 2" stroke="#8cc63f" stroke-width="2" fill="none"/></svg>ROBUST, <small>but still powerful</small></li>
    <li><svg width="10" height="10"><path d="M1 5 L4 8 L9 2" stroke="#8cc63f" stroke-width="2" fill="none"/></svg>SECURE, <small>know we're safe</small></li>
    <li><svg width="10" height="10"><path d="M1 5 L4 8 L9 2" stroke="#8cc63f" stroke-width="2" fill="none"/></svg>VERSATILE, <small>fits any venue type</small></li>
    <li><svg width="10" height="10"><path d="M1 5 L4 8 L9 2" stroke="#8cc63f" stroke-width="2" fill="none"/></svg>AFFORDABLE, <small>fair priced</small></li>
  </ul>
</section>

<section class="pricing">
  <div class="plans">
    <div class="plan">
      <h3>STANDARD</h3>
      <div class="price">FREE!</div>
      <ul>
        <li>✔ Fully functional scheduling tool</li>
        <li>✔ Videos for easy viewing</li>
        <li>✔ Web based login anywhere</li>
        <li>✔ Trial students &amp; instructors</li>
        <li>✔ Unlimited class listings</li>
        <li>✔ Online class booking</li>
        <li>✔ Bookkeeping &amp; attendance</li>
        <li>✔ Class reports</li>
        <li>✔ Basic data backups</li>
        <li>✔ 1 user account</li>
        <li>✔ Email support</li>
        <li>✔ No credit card required</li>
      </ul>
    </div>
    <div class="plan featured">
      <h3>PREMIUM</h3>
      <div class="price">$39<small>/month</small></div>
      <ul>
        <li>✔ 5 User Accounts</li>
        <li>✔ Unlimited Logins</li>
        <li>✔ Collaborative File Sharing</li>
        <li>✔ Activity Feed: Track Your Studio</li>
        <li>✔ Activity Feed: Discussion Board</li>
        <li>✔ Reports: Attendance Sheets</li>
        <li>✔ Reports: Instructor Schedules</li>
        <li>✔ Reports: Income &amp; Expenses</li>
        <li>✔ Best in Class Phone Support</li>
      </ul>
    </div>
    <div class="plan">
      <h3>PROFESSIONAL</h3>
      <div class="price">$79<small>/month</small></div>
      <ul>
        <li>✔ Powerful Point of Sale System</li>
        <li>✔ Accept Credit Cards Immediately</li>
        <li>✔ Web Based Self-Serve Options Online</li>
        <li>✔ Easily Publish Your Schedule Online</li>
        <li>✔ Sell Retail Goods, Passes, and More</li>
        <li>✔ Mailing List Integration</li>
        <li>✔ Accounting Integration</li>
        <li>✔ Add User Accounts for $5</li>
        <li>✔ Priority Customer Support</li>
      </ul>
    </div>
  </div>
  <div class="trial"><span>FREE</span><b>30</b><span>DAY TRIAL</span></div>
</section>

<footer class="site-footer">
  <div class="footer-row">
    <div class="footer-links"><span>About</span>|<span>Terms</span>|<span>FAQ</span>|<span>Contact</span>|<span>Upcoming</span>|<span>Videos</span>|<span>Affiliates</span></div>
    <div>Connect with us</div>
  </div>
  <p class="copyright">Copyright MoveNest.com, All Rights Reserved.</p>
</footer>

</div>
</body>
</html>
```